Monthly Wall Calendar for Brinvale Paws Rescue

We will provide photo's description of dogs and placement of photos and all written material for calendar. We need a wall calendar and we will need as a final output pdf files with the proper bleed lines to send to printer. We have uploaded what the prior year calendar looked like. We are looking for something similar this year.

Generally there is a large monthly photo and 2-3 smaller ones added to the calendar page.

Target Market(s)

Our supporters and animal rescue people.

Font styles to use
Serif

Colors
6c459b
b7a5cd

Requirements
Must have
• A final pdf file with bleed lines for printer.
Nice to have
• The uploaded calendar gives a nice idea of what we are looking for as well as this link. http://brinvalepaws.com/calendar-2016-photo-spread/ and http://brinvalepaws.com/covers-2017/
Should not have
• Not cluttered

```html
<!DOCTYPE html>
<html lang="en">
<head>
<meta charset="utf-8">
<title>Brinvale Paws Rescue · January 2018</title>
<link rel="stylesheet" href="https://fonts.googleapis.com/css2?family=Oswald:wght@400;500&family=Open+Sans:wght@400;600&family=Montserrat:wght@800&display=swap">
<style>
  :root {
    --purple: #5b3f8a;
    --purple-brand: #6c459b;
    --lilac: #b7a5cd;
    --ink: #555555;
    --chip-dark: #545454;
    --cell: #f0f0f0;
    --white: #ffffff;
  }
  * { box-sizing: border-box; margin: 0; padding: 0; }
  html, body { width: 733px; height: 1200px; overflow: hidden; background: var(--white); }
  .calendar-page { position: relative; width: 733px; height: 1200px; overflow: hidden; font-family: "Open Sans", sans-serif; }

  .hero-photo {
    position: absolute; left: 0; top: 0; width: 733px; height: 598px;
    background:
      radial-gradient(ellipse 190px 300px at 440px 330px, #b89a82 0%, #8a6c5c 55%, transparent 100%),
      radial-gradient(circle at 110px 150px, #7e9aa0 0%, transparent 35%),
      radial-gradient(circle at 650px 220px, #8d6a9a 0%, transparent 40%),
      linear-gradient(135deg, #4a4b52 0%, #5e4a6a 45%, #6a4f7a 75%, #7a5f8a 100%);
  }
  .dog-story { position: absolute; left: 26px; top: 413px; padding-left: 12px; border-left: 4px solid var(--white); width: 216px; height: 133px; }
  .dog-name { font-family: "Montserrat", sans-serif; font-weight: 800; font-size: 33px; line-height: 30px; color: var(--white); letter-spacing: 0.5px; }
  .dog-bio { margin-top: 4px; font-size: 8.7px; line-height: 11.3px; color: var(--white); text-align: justify; }
  .dog-head-art { position: absolute; left: 155px; top: 323px; width: 80px; height: 115px; border-radius: 40% 40% 45% 45%; background: linear-gradient(160deg, var(--lilac), #8c74b0); opacity: 0.9; }

  .rescue-mark { position: absolute; left: 600px; top: 520px; width: 110px; text-align: center; color: var(--white); }
  .rescue-mark .dot { display: block; width: 40px; height: 40px; margin: 0 auto 8px; border-radius: 50%; background: #333333; }
  .rescue-mark .name { font-size: 9.5px; font-weight: 600; color: #e9e3ef; }

  .band-photo {
    position: absolute; left: 0; top: 598px; width: 733px; height: 231px;
    background:
      radial-gradient(ellipse 60px 90px at 280px 710px, #e8e4de 0%, transparent 100%),
      linear-gradient(180deg, #2b2a22 0%, #3d4526 40%, #5d7a2e 75%, #6f8f36 100%);
  }
  .band-photo-art { position: absolute; inset: 0; }

  .month-label { position: absolute; left: 35px; top: 762px; width: 216px; height: 66px; background: var(--purple); border: 3px solid var(--white); border-radius: 10px; font-family: "Oswald", sans-serif; font-weight: 500; font-size: 46px; line-height: 58px; color: var(--white); text-align: center; letter-spacing: 1px; }
  .year-label { position: absolute; left: 446px; top: 716px; font-family: "Montserrat", sans-serif; font-weight: 800; font-size: 114px; line-height: 120px; color: var(--white); letter-spacing: -3px; }

  .month-grid { position: absolute; left: 17px; top: 846px; display: grid; grid-template-columns: repeat(7, 42px); column-gap: 15.5px; row-gap: 7px; grid-template-rows: 42px repeat(6, 42px); }
  .weekday { border-radius: 8px; background: var(--chip-dark); color: var(--white); font-family: "Oswald", sans-serif; font-size: 19px; line-height: 42px; text-align: center; }
  .weekday.weekend { background: var(--purple); }
  .day { border-radius: 8px; background: var(--cell); color: var(--ink); font-family: "Open Sans", sans-serif; font-size: 22px; line-height: 42px; text-align: center; }
  .day.weekend { color: var(--purple); }
  .day.blank { color: transparent; }
  .day-photo { border-radius: 8px; }
  .day-photo.wide { grid-column: 3 / span 3; background: linear-gradient(90deg, #8aa052, #5b4630 50%, #9fb562); }
  .day-photo.small { grid-column: 6 / span 2; background: linear-gradient(180deg, #6a7d3a, #e8e6e0 55%, #7f9440); }
  .month-grid .gap-fill { margin-top: 7px; }

  .holidays { position: absolute; left: 472px; top: 838px; list-style: none; font-family: "Open Sans", sans-serif; font-size: 11px; line-height: 14px; color: #333333; font-weight: 600; letter-spacing: 0.3px; }
  .holidays .date { color: var(--purple-brand); }

  .mini-month { position: absolute; left: 471px; width: 196px; border: 2px solid var(--ink); border-radius: 12px; padding: 6px 10px 6px 18px; }
  .mini-month.prev { top: 891px; height: 146px; }
  .mini-month.next { top: 1049px; height: 128px; }
  .mini-title { font-family: "Oswald", sans-serif; font-size: 13px; line-height: 16px; color: #333333; }
  .mini-title .year { color: var(--purple-brand); }
  .mini-grid { display: grid; grid-template-columns: repeat(7, 23.5px); row-gap: 3px; margin-top: 2px; }
  .mini-grid .wd { width: 19px; height: 15px; border-radius: 3px; background: var(--chip-dark); color: var(--white); font-size: 8px; line-height: 15px; text-align: center; margin-bottom: 3px; }
  .mini-grid .wd.weekend { background: var(--purple-brand); }
  .mini-grid .d { width: 19px; font-size: 9px; line-height: 13px; text-align: center; color: #333333; }
  .mini-grid .d.weekend { color: var(--purple-brand); }
</style>
</head>
<body>
<main class="calendar-page">
  <div class="hero-photo" role="img" aria-label="Photo of Gibbs, a long-haired German shepherd, smiling in a sunlit forest"></div>
  <div class="dog-head-art" role="img" aria-label="Lilac illustrated shepherd head emblem"></div>
  <section class="dog-story">
    <h1 class="dog-name">GIBBS</h1>
    <p class="dog-bio">Gibbs was found as a stray, just looking for someone to be his best friend. He came to us with a big smile and a desire for love and attention. Gibbs also had chronic ear infections which required constant medical care. He is now enjoying his new family and being able to run, play and just be a happy dog.</p>
  </section>
  <div class="rescue-mark"><span class="dot"></span><span class="name">brinvalepaws.com</span></div>

  <div class="band-photo" role="img" aria-label="Photo of a white shepherd puppy sitting in tall summer grass"></div>

  <div class="month-label">JANUARY</div>
  <div class="year-label">2018</div>

  <section class="month-grid" aria-label="January 2018">
    <div class="weekday weekend">Su</div><div class="weekday">Mo</div><div class="weekday">Tu</div><div class="weekday">We</div><div class="weekday">Th</div><div class="weekday">Fr</div><div class="weekday weekend">Sa</div>
    <div class="day blank"></div><div class="day blank"></div><div class="day blank"></div><div class="day blank"></div><div class="day blank"></div><div class="day blank"></div><div class="day weekend">1</div>
    <div class="day weekend">2</div><div class="day">3</div><div class="day">4</div><div class="day">5</div><div class="day">6</div><div class="day">7</div><div class="day weekend">8</div>
    <div class="day weekend">9</div><div class="day">10</div><div class="day">11</div><div class="day">12</div><div class="day">13</div><div class="day">14</div><div class="day weekend">15</div>
    <div class="day weekend">16</div><div class="day">17</div><div class="day">18</div><div class="day">19</div><div class="day">20</div><div class="day">21</div><div class="day weekend">22</div>
    <div class="day weekend">23</div><div class="day">24</div><div class="day">25</div><div class="day">26</div><div class="day">27</div><div class="day">28</div><div class="day weekend">29</div>
    <div class="day weekend">30</div><div class="day">31</div>
    <div class="day-photo wide" role="img" aria-label="Photo of a shepherd lying on the lawn"></div>
    <div class="day-photo small" role="img" aria-label="Photo of a white shepherd running across a field"></div>
  </section>

  <ul class="holidays">
    <li><span class="date">Jan 01</span> &gt; New Years Day</li>
    <li><span class="date">Jan 16</span> &gt; Martin Luther King day</li>
    <li><span class="date">Jan 17</span> &gt; Elias Harrow Birthday</li>
  </ul>

  <section class="mini-month prev" aria-label="December 2017">
    <h2 class="mini-title">DECEMBER <span class="year">2017</span></h2>
    <div class="mini-grid">
      <span class="wd weekend">Su</span><span class="wd">Mo</span><span class="wd">Tu</span><span class="wd">We</span><span class="wd">Th</span><span class="wd">Fr</span><span class="wd weekend">Sa</span>
      <span class="d"></span><span class="d"></span><span class="d"></span><span class="d"></span><span class="d"></span><span class="d">1</span><span class="d weekend">2</span>
      <span class="d weekend">3</span><span class="d">4</span><span class="d">5</span><span class="d">6</span><span class="d">7</span><span class="d">8</span><span class="d weekend">9</span>
      <span class="d weekend">10</span><span class="d">11</span><span class="d">12</span><span class="d">13</span><span class="d">14</span><span class="d">15</span><span class="d weekend">16</span>
      <span class="d weekend">17</span><span class="d">18</span><span class="d">19</span><span class="d">20</span><span class="d">21</span><span class="d">22</span><span class="d weekend">23</span>
      <span class="d weekend">24</span><span class="d">25</span><span class="d">26</span><span class="d">27</span><span class="d">28</span><span class="d">29</span><span class="d weekend">30</span>
      <span class="d weekend">31</span>
    </div>
  </section>

  <section class="mini-month next" aria-label="February 2018">
    <h2 class="mini-title">FEBUARY <span class="year">2018</span></h2>
    <div class="mini-grid">
      <span class="wd weekend">Su</span><span class="wd">Mo</span><span class="wd">Tu</span><span class="wd">We</span><span class="wd">Th</span><span class="wd">Fr</span><span class="wd weekend">Sa</span>
      <span class="d"></span><span class="d"></span><span class="d"></span><span class="d">1</span><span class="d">2</span><span class="d">3</span><span class="d weekend">4</span>
      <span class="d weekend">5</span><span class="d">6</span><span class="d">7</span><span class="d">8</span><span class="d">9</span><span class="d">10</span><span class="d weekend">11</span>
      <span class="d weekend">12</span><span class="d">13</span><span class="d">14</span><span class="d">15</span><span class="d">16</span><span class="d">17</span><span class="d weekend">18</span>
      <span class="d weekend">19</span><span class="d">20</span><span class="d">21</span><span class="d">22</span><span class="d">23</span><span class="d">24</span><span class="d weekend">25</span>
      <span class="d weekend">26</span><span class="d">27</span><span class="d">28</span>
    </div>
  </section>
</main>
</body>
</html>
```